Chinese Language Posters - TKUOME

We have created a series of African American heritage posters that will be distributed to Chinese Language Schools. We need a designer to create great posters for K-12 programs.

Quotes:
We have quotes from 6 important figures in Black History. We are seeking a designer to develop a poster utilizing at least one quote from each historical figure.

The designer MUST be fluent in Chinese in order to ensure the appropriate type and font.

Our organization, Tidewater Kestrel Union of Orchard Mentors Exchange, is a small organization of parents in the Bay Area working to encourage and support Black students learning the Chinese language.

Target Market(s)

These posters will be made available to Chinese Immersion schools (k-12).

Industry/Entity Type

Learning

Requirements
Must have
• Each poster should contain one quote from the list below.

Please create a poster of one historical figure and include their quote. The image can be abstract, landscape or an image of the figure.

The image should also include our logo. Our preferred logo is with the puffs but we understand if the clipart logo may be a better fit for the posters. (We LOVE the puffs logo though).
Nice to have
• I have uploaded images of each figure. The images can be used or a more abstract background. We are flexible. We would prefer a mix that includes figures and abstract backgrounds just focusing on the quote. We are open.

```html
<!DOCTYPE html>
<html lang="zh-CN">
<head>
<meta charset="utf-8">
<title>TKUOME — 信念就是跨出第一步</title>
<link rel="stylesheet" href="https://fonts.googleapis.com/css2?family=Noto+Sans+SC:wght@400;500&family=Roboto+Condensed:wght@300;400&display=swap">
<style>
  :root {
    --red-bright: #e0100f;
    --red-mid: #a80807;
    --red-deep: #4a0202;
    --black: #000000;
    --white: #ffffff;
    --brand-red: #d8141a;
  }
  * { margin: 0; padding: 0; box-sizing: border-box; }
  html, body {
    width: 849px;
    height: 1200px;
    overflow: hidden;
    background: var(--black);
  }
  .poster {
    position: relative;
    width: 849px;
    height: 1200px;
    overflow: hidden;
    background: var(--black);
  }
  .portrait-field {
    position: absolute;
    inset: 0;
    background:
      radial-gradient(ellipse 60% 48% at 58% 40%, var(--red-bright) 0%, rgba(200, 10, 10, 0.85) 45%, rgba(120, 4, 4, 0) 100%),
      linear-gradient(180deg, var(--red-deep) 0%, var(--red-mid) 22%, var(--red-bright) 55%, var(--red-mid) 78%, #1a0000 100%);
  }
  .portrait-field::after {
    content: "";
    position: absolute;
    inset: 0;
    background: radial-gradient(ellipse 85% 80% at 55% 45%, rgba(0,0,0,0) 55%, rgba(0,0,0,0.75) 100%);
  }
  .quote {
    position: absolute;
    left: 41px;
    top: 761px;
    font-family: "Noto Sans SC", sans-serif;
    color: var(--white);
  }
  .quote-line {
    display: block;
    width: max-content;
    background: var(--black);
    line-height: 1;
  }
  .quote-line--first {
    font-size: 44px;
    padding: 10px 6px 11px 10px;
    margin-bottom: 8px;
    letter-spacing: 0.5px;
  }
  .quote-line--second {
    font-size: 58px;
    padding: 9px 6px 9px 6px;
    letter-spacing: 0.5px;
  }
  .brand-block {
    position: absolute;
    left: 423px;
    top: 1051px;
    width: 426px;
    height: 149px;
    background: var(--black);
  }
  .brand-mark {
    position: absolute;
    left: 18px;
    top: 26px;
    width: 96px;
    height: 96px;
    border-radius: 50%;
    background: var(--brand-red);
  }
  .brand-name {
    position: absolute;
    left: 130px;
    top: 22px;
    font-family: "Roboto Condensed", sans-serif;
    font-weight: 300;
    font-size: 80px;
    line-height: 1;
    color: var(--white);
    letter-spacing: 1px;
  }
  .brand-tagline {
    position: absolute;
    left: 131px;
    top: 110px;
    font-family: "Roboto Condensed", sans-serif;
    font-weight: 300;
    font-size: 10.5px;
    color: var(--white);
    white-space: nowrap;
  }
</style>
</head>
<body>
  <main class="poster">
    <div class="portrait-field" role="img" aria-label="Red-toned portrait photograph of a civil rights leader in a dark suit and tie, looking upward"></div>

    <p class="quote">
      <span class="quote-line quote-line--first">信念就是跨出第一步,</span>
      <span class="quote-line quote-line--second">哪怕你看不到整个楼梯。</span>
    </p>

    <footer class="brand-block">
      <span class="brand-mark" aria-hidden="true"></span>
      <span class="brand-name">TKUOME</span>
      <span class="brand-tagline">Tidewater Kestrel Union of Orchard Mentors Exchange</span>
    </footer>
  </main>
</body>
</html>
```